Bookcover: Lessons From the Silent Orchard

I am publishing a super-low-cost innovation book for €4,99 on Bravolo Self Release to help everyone become a great innovator: young ambitious people without college education nor a big budget. Do you want to help me?

Brief:
Design a book cover 1600 x 2560 pixels for BSR.
Main title: Lessons From the Silent Orchard
Sub title: mindset - insights - skills & tools
Author: Maarten de Klerk
Design: captive, and appealing to everyone
Target Group: young ambitious people without college education

For bravolo please format the height/width ratio of 1.6:1

```html
<!DOCTYPE html>
<html lang="en">
<head>
<meta charset="utf-8">
<title>Lessons From the Silent Orchard — Book Cover</title>
<link rel="stylesheet" href="https://fonts.googleapis.com/css2?family=Montserrat:wght@800;900&family=Barlow+Semi+Condensed:wght@800&display=swap">
<style>
  :root {
    --paper: #ffffff;
    --cream: #fdefcc;
    --plum: #5c2f66;
    --berry: #9a4a73;
    --sun: #fdb900;
    --rose: #c0688f;
  }
  * { margin: 0; padding: 0; box-sizing: border-box; }
  html, body { width: 750px; height: 1200px; overflow: hidden; background: var(--paper); }
  .cover {
    position: relative;
    width: 750px;
    height: 1200px;
    overflow: hidden;
    background: var(--paper);
  }
  .backdrop { position: absolute; inset: 0; }
  .author {
    position: absolute;
    top: 62px;
    left: 0;
    width: 750px;
    text-align: center;
    font-family: "Montserrat", sans-serif;
    font-weight: 900;
    font-size: 46px;
    line-height: 1;
    letter-spacing: -0.5px;
    color: var(--plum);
  }
  .author-rule {
    position: absolute;
    top: 114px;
    left: 190px;
    width: 375px;
    height: 2px;
    background: var(--plum);
  }
  .title {
    position: absolute;
    top: 516px;
    left: 0;
    width: 750px;
    text-align: center;
    font-family: "Montserrat", sans-serif;
    font-weight: 800;
    font-size: 94px;
    line-height: 85px;
    letter-spacing: -1px;
    color: var(--berry);
  }
  .title span { display: block; }
  .subtitle {
    position: absolute;
    top: 886px;
    left: 145px;
    width: 462px;
    text-align: center;
    font-family: "Barlow Semi Condensed", sans-serif;
    font-weight: 800;
    font-size: 29px;
    line-height: 1;
    color: var(--plum);
    white-space: nowrap;
  }
  .art { position: absolute; }
  .bulb-art {
    left: 226px; top: 164px; width: 300px; height: 348px;
    border-radius: 24px;
    background: radial-gradient(circle at 50% 42%, var(--sun) 0 45%, rgba(253,185,0,0.25) 70%, rgba(253,185,0,0) 100%);
  }
  .leaf-art {
    left: 75px; top: 880px; width: 60px; height: 52px;
    border-radius: 14px;
    background: linear-gradient(135deg, var(--sun), var(--rose));
    opacity: 0.75;
  }
  .flight-art {
    left: 75px; top: 940px; width: 365px; height: 218px;
    border-radius: 18px;
    background: linear-gradient(160deg, rgba(253,185,0,0.18), rgba(192,104,143,0.28));
  }
</style>
</head>
<body>
<main class="cover">
  <svg class="backdrop" width="750" height="1200" viewBox="0 0 750 1200" aria-hidden="true">
    <path fill="var(--cream)" d="M0 337 C50 305 120 296 180 304 C270 316 300 380 350 430 C380 458 420 460 450 430 C490 390 510 320 550 290 C600 260 660 250 750 377 L750 1200 L0 1200 Z"/>
  </svg>

  <h2 class="author">MAARTEN DE KLERK</h2>
  <div class="author-rule"></div>

  <div class="art bulb-art" role="img" aria-label="Illustration of a glowing light bulb with rays"></div>

  <h1 class="title">
    <span>LESSONS</span>
    <span>FROM THE</span>
    <span>SILENT</span>
    <span>ORCHARD</span>
  </h1>

  <div class="art leaf-art" role="img" aria-label="Small decorative leaves and dot"></div>

  <p class="subtitle">MINDSET - INSIGHTS - SKILLS &amp; TOOLS</p>

  <div class="art flight-art" role="img" aria-label="Illustration of a paper plane with a looping dashed flight path"></div>
</main>
</body>
</html>
```